Plumbing and Fire Protection Consulting Engineering

Business Cards for one person plumbing and fire protection engineering consulting business based in NJ, serving mostly New York City:
Ravel Consulting, Plumbing and Fire Protection Engineering
Martin Kolbeck- President
52-07 Danforth Street, Fair Lawn, NJ 07563
201-486-2713
ravelpipework@ravelmail.example

Target Market(s)

- Private Building Developers, looking to reduce construction cost
- MEP (Mechanical, Electrical, Plumbing) Design Engineers that have staff shortage, need temporary help, advise, drawings quality control
- Architects that need advise on plumbing or fire protection
- Any of the above that need opinion on disputed construction costs, change orders, construction observation reports

Industry/Entity Type

Business

Contact Information for Business Card

Logo and business card should include (other suggestions welcome):
- A plumbing symbol, like pipe or wrench or similar
- Fire Protection symbol, like fire sprinkler
- Dollar signs $$$$$ in descending font sizes suggesting construction cost reduction as a result of my work. or some other symbol of economic design
- Symbol of engineering
- High rise building(s) or Manhattan skyline on the background, maybe building under construction.
- Maybe a building floor plan design (preferably old, not modern, like in Michelangelo or Gaudi sketches)

Font styles to use
Sans Serif

Colors

Designer to choose colors to be used in the design.

Requirements
Must have
• A card that is unique, unlike any others- like my business is.
• My name, business name, address, phone, email, see description
Nice to have
• Something that suggests 30+ years experience in this field, not sure how to convey this message.
• Maybe my Linkedin picture with Statue of Liberty on the background (attached) is good to have, but i am not sure- not insisting on that.
Should not have
• Symbols that not related to engineering design and construction- like fire truck, funny plumbers figures and symbols, toilets, etc.
• Computer symbols. I am not trying to impress clients with my computer skills, not my selling point

```html
<!DOCTYPE html>
<html lang="en">
<head>
<meta charset="utf-8">
<title>Ravel Consulting – Business Card</title>
<link href="https://fonts.googleapis.com/css2?family=Roboto:wght@400;500;700&display=swap" rel="stylesheet">
<style>
  :root {
    --stage: #d3d3d3;
    --stage-light: #ececec;
    --ink: #1b1b1b;
    --brand-blue: #1f6fd1;
    --deep-blue: #2a3c9e;
    --sky-blue: #0d94e2;
    --brand-orange: #f27a1a;
    --gold: #d8ad3c;
    --gold-dark: #8a6514;
    --night: #1c1c1c;
    --night-light: #3a3a3a;
    --muted-grey: #a9a9a9;
  }
  * { margin: 0; padding: 0; box-sizing: border-box; }
  html, body { width: 900px; height: 1200px; overflow: hidden; }
  body {
    font-family: "Roboto", Arial, sans-serif;
    background: radial-gradient(ellipse at center, var(--stage-light) 0%, var(--stage) 75%);
    position: relative;
  }
  .card {
    position: absolute;
    left: 82px;
    width: 733px;
    height: 430px;
    border-radius: 22px;
    overflow: hidden;
    box-shadow: 0 6px 14px rgba(0,0,0,.25);
  }
  .card--front { top: 137px; background: #fff; }
  .card--back { top: 633px; }

  .skyline-photo { position: absolute; inset: 0; }
  .card--front .skyline-photo {
    background: linear-gradient(180deg, #fbfbfb 0%, #f1f1f1 35%, #dcdcdc 65%, #cfd0d2 100%);
  }
  .card--back .skyline-photo {
    background: linear-gradient(180deg, var(--night) 0%, #262626 40%, var(--night-light) 75%, #2a2a2a 100%);
  }

  .holder { position: absolute; left: 41px; top: 60px; }
  .holder__name { font-size: 20px; font-weight: 500; color: var(--ink); }
  .holder__title { font-size: 17px; color: var(--brand-orange); margin-top: 4px; }
  .holder__rule { position: absolute; left: 0; top: 118px; width: 248px; height: 3px;
    background: linear-gradient(90deg, var(--brand-orange) 0 41px, var(--deep-blue) 41px 100%); }

  .brand { position: absolute; display: flex; align-items: center; }
  .brand__dot { border-radius: 50%; flex: none; }
  .brand__name { font-weight: 700; line-height: 1; letter-spacing: .2px; }
  .brand__tagline { font-weight: 500; line-height: 1; margin-top: 6px; }

  .card--front .brand { left: 296px; top: 48px; }
  .card--front .brand__dot { width: 62px; height: 62px; background: var(--brand-blue); margin-right: 24px; }
  .card--front .brand__name { font-size: 33px; color: var(--brand-blue); }
  .card--front .brand__tagline { font-size: 15px; color: var(--brand-orange); }

  .card--back .brand { left: 121px; top: 168px; }
  .card--back .brand__dot { width: 70px; height: 70px; background: #fff; margin-right: 24px; }
  .card--back .brand__name { font-size: 40px; color: #fff; }
  .card--back .brand__tagline { font-size: 18px; color: var(--muted-grey); margin-top: 8px; }

  .contact { position: absolute; left: 41px; top: 283px; list-style: none; }
  .contact__item { display: flex; align-items: center; font-size: 15.5px; color: var(--ink); height: 24.5px; }
  .contact__icon { width: 16px; height: 16px; margin-right: 8px; fill: var(--deep-blue); }

  .swoosh { position: absolute; left: 0; bottom: 0; width: 733px; height: 430px; }

  .seal { position: absolute; left: 603px; top: 301px; width: 90px; height: 90px; }
</style>
</head>
<body>

<section class="card card--front" aria-label="Business card front">
  <div class="skyline-photo" role="img" aria-label="Faded photograph of a city skyline of high-rise towers"></div>

  <svg class="swoosh" viewBox="0 0 733 430" aria-hidden="true">
    <defs>
      <linearGradient id="band-blue" x1="0" x2="1" y1="0" y2="0">
        <stop offset="0" stop-color="#2a3c9e"/>
        <stop offset="0.5" stop-color="#1f6fd1"/>
        <stop offset="1" stop-color="#0d94e2"/>
      </linearGradient>
      <linearGradient id="band-orange" x1="0" x2="1" y1="0" y2="0">
        <stop offset="0" stop-color="#e2481b"/>
        <stop offset="0.6" stop-color="#f27a1a"/>
        <stop offset="1" stop-color="#f9b01c"/>
      </linearGradient>
    </defs>
    <path d="M0,396 Q320,396 520,366 Q650,345 733,312 L733,336 Q650,362 520,380 Q320,404 0,402 Z" fill="url(#band-orange)"/>
    <path d="M0,405 Q320,408 520,386 Q650,370 733,342 L733,430 L0,430 Z" fill="#fff"/>
    <path d="M0,410 Q320,413 520,392 Q650,377 733,348 L733,430 L0,430 Z" fill="url(#band-blue)"/>
  </svg>

  <div class="holder">
    <p class="holder__name">Martin Kolbeck</p>
    <p class="holder__title">President</p>
  </div>
  <div class="holder__rule" style="left:0;top:118px;"></div>

  <div class="brand">
    <span class="brand__dot"></span>
    <div>
      <p class="brand__name">RAVEL CONSULTING</p>
      <p class="brand__tagline">Plumbing and Fire Protection Engineering</p>
    </div>
  </div>

  <ul class="contact">
    <li class="contact__item">
      <svg class="contact__icon" viewBox="0 0 24 24"><path d="M3 9c0-3 4-5 9-5s9 2 9 5v2h-5V8.5c-1-.5-2.5-.8-4-.8s-3 .3-4 .8V11H3z M5 13h14l1 7H4z"/></svg>
      201-486-2713
    </li>
    <li class="contact__item">
      <svg class="contact__icon" viewBox="0 0 24 24"><path d="M2 5h20v14H2z" /><path d="M2 5l10 8 10-8" fill="none" stroke="#fff" stroke-width="2"/></svg>
      ravelpipework@ravelmail.example
    </li>
    <li class="contact__item">
      <svg class="contact__icon" viewBox="0 0 24 24"><path d="M12 2a7 7 0 0 0-7 7c0 5 7 13 7 13s7-8 7-13a7 7 0 0 0-7-7zm0 9.5a2.5 2.5 0 1 1 0-5 2.5 2.5 0 0 1 0 5z"/></svg>
      52-07 Danforth Street, Fair Lawn, NJ 07563
    </li>
  </ul>

  <svg class="seal" viewBox="0 0 90 90" aria-label="30 years experience seal">
    <circle cx="45" cy="45" r="44" fill="#d8ad3c"/>
    <circle cx="45" cy="45" r="38" fill="#8a6514"/>
    <circle cx="45" cy="45" r="35" fill="#1e1a12"/>
    <circle cx="45" cy="45" r="25" fill="none" stroke="#d8ad3c" stroke-width="1.5"/>
    <text x="45" y="48" text-anchor="middle" font-family="Roboto, Arial, sans-serif" font-weight="700" font-size="22" fill="#e6c260">30</text>
    <text x="45" y="60" text-anchor="middle" font-family="Roboto, Arial, sans-serif" font-weight="700" font-size="8" fill="#e6c260">YEARS</text>
  </svg>
</section>

<section class="card card--back" aria-label="Business card back">
  <div class="skyline-photo" role="img" aria-label="Dark monochrome photograph of a city skyline of skyscrapers"></div>
  <div class="brand">
    <span class="brand__dot"></span>
    <div>
      <p class="brand__name">RAVEL CONSULTING</p>
      <p class="brand__tagline">Plumbing and Fire Protection Engineering</p>
    </div>
  </div>
</section>

</body>
</html>
```